Brookfell Self Storage - Business Sign

The sign we are needing designed is our main road sign for our self-storage business. The dimensions of the sign are 57 inches tall x 96 inches wide. We require that our attached logo be on the sign as well as our phone number: 478-216-4387 and website www.BrookfellStorage.net. Optional information that can be added but not required is our address: 418 Marlow Tenney Pkwy, Centerville, GA 31047.

Industry/Entity Type

Self Storage

Font styles to use
Sans Serif

```html
<!DOCTYPE html>
<html lang="en">
<head>
<meta charset="utf-8">
<title>Brookfell Self Storage – Road Sign</title>
<link href="https://fonts.googleapis.com/css2?family=Outfit:wght@600;700&display=swap" rel="stylesheet">
<style>
  :root {
    --page-bg: #f4f5f7;
    --sign-blue-deep: #1665d0;
    --sign-blue-mid: #3d97ec;
    --sign-blue-light: #a9d2f8;
    --sign-white: #ffffff;
    --ink: #454545;
  }
  html, body {
    margin: 0;
    padding: 0;
    width: 988px;
    height: 1200px;
    overflow: hidden;
    background: var(--page-bg);
  }
  .canvas {
    width: 988px;
    height: 1200px;
    display: flex;
    align-items: center;
    justify-content: center;
  }
  .road-sign {
    width: 904px;
    height: 537px;
    box-sizing: border-box;
    background: linear-gradient(180deg,
      var(--sign-blue-deep) 0%,
      var(--sign-blue-mid) 45%,
      var(--sign-blue-light) 75%,
      var(--sign-white) 100%);
    display: flex;
    flex-direction: column;
    align-items: center;
    justify-content: center;
    padding: 30px 40px;
    font-family: "Outfit", sans-serif;
    color: var(--ink);
    text-align: center;
  }
  .business-name {
    margin: 0 0 34px;
    background: var(--sign-white);
    padding: 18px 56px 22px;
    font-size: 80px;
    font-weight: 700;
    line-height: 1.02;
    letter-spacing: 1px;
    color: var(--ink);
  }
  .phone-number {
    margin: 0;
    font-size: 64px;
    font-weight: 700;
    letter-spacing: 2px;
    line-height: 1.1;
  }
  .website {
    margin: 6px 0 0;
    font-size: 42px;
    font-weight: 700;
    letter-spacing: 1.5px;
    text-transform: uppercase;
    line-height: 1.1;
  }
</style>
</head>
<body>
  <main class="canvas">
    <section class="road-sign" aria-label="Brookfell Self Storage road sign">
      <h1 class="business-name">Brookfell<br>Self Storage</h1>
      <p class="phone-number">478-216-4387</p>
      <p class="website">BrookfellStorage.net</p>
    </section>
  </main>
</body>
</html>
```